R.Tamo Fiji Limited

to create a master letter head with 35 years of fijian owned
Company boilerplate (for proposals/emails)
R. Tamo Fiji Limited is a respected Fijian company with 35 years of continuous service to our communities across the Pacific. We deliver end-to-end manufacturing and engineering, commercial refrigeration & air-conditioning, property development/management, and mobility solutions. As a distributor of Q-R-VU golf carts and Maplor batteries, we support resorts, airports, and industries with reliable supply, parts, and after-sales service. Built on craftsmanship, integrity, and community, R. Tamo has become a household name in Fiji.
About-us paragraph (website “About”)
For 35 years, R. Tamo Fiji Limited has been a pillar of the local economy and a trusted partner throughout the Pacific Islands. Our group combines precision manufacturing and stainless-steel fabrication with refrigeration & air-conditioning projects, real-estate development, and golf-cart fleets and energy systems. We proudly distribute Q-R-VU golf carts and Maplor batteries, and we back every sale with responsive technical support. Our promise is simple: reliable quality, fair value, and long-term support for every client.
Group Buiness

```html
<!DOCTYPE html>
<html lang="en">
<head>
<meta charset="utf-8">
<title>R.Tamo Fiji Limited — Letterhead</title>
<link href="https://fonts.googleapis.com/css2?family=Nunito:wght@400;600;800&display=swap" rel="stylesheet">
<style>
  :root {
    --backdrop: #a2a9a5;
    --paper: #f1f1f1;
    --navy: #133a6d;
    --amber: #f0a122;
    --ink-light: #ffffff;
    --watermark: #dcdcdc;
  }
  * { margin: 0; padding: 0; box-sizing: border-box; }
  html, body {
    width: 1200px;
    height: 803px;
    overflow: hidden;
    background: var(--backdrop);
    font-family: "Nunito", sans-serif;
  }
  .letterhead {
    position: absolute;
    left: 330px;
    top: 20px;
    width: 540px;
    height: 763px;
    background: var(--paper);
    box-shadow: 0 6px 18px rgba(0, 0, 0, 0.25);
    overflow: hidden;
  }
  .letterhead__bands {
    position: absolute;
    inset: 0;
    width: 100%;
    height: 100%;
  }
  .band--navy { fill: var(--navy); }
  .band--amber { fill: var(--amber); }

  .contact {
    position: absolute;
    left: 396px;
    top: 21px;
    list-style: none;
    color: var(--ink-light);
    font-size: 8.5px;
    font-weight: 600;
    line-height: 13px;
  }
  .contact__item {
    display: flex;
    align-items: center;
    gap: 4px;
  }
  .contact__icon {
    width: 7px;
    height: 7px;
    fill: none;
    stroke: var(--ink-light);
    stroke-width: 1.4;
  }
  .contact__icon--solid { fill: var(--ink-light); stroke: none; }

  .brand {
    position: absolute;
    left: 40px;
    top: 86px;
    color: var(--navy);
    font-weight: 800;
    font-size: 20px;
    letter-spacing: 0.3px;
  }

  .watermark {
    position: absolute;
    left: 0;
    right: 0;
    top: 330px;
    text-align: center;
    color: var(--watermark);
    font-weight: 800;
    font-size: 64px;
    letter-spacing: 1px;
  }
</style>
</head>
<body>
  <main class="letterhead">
    <svg class="letterhead__bands" viewBox="0 0 686 960" preserveAspectRatio="none" aria-hidden="true">
      <path class="band--amber" d="M0,0 H686 V132 C470,96 230,80 0,89 Z"/>
      <path class="band--navy" d="M0,0 H686 V132 C520,88 280,26 0,40 Z"/>
      <path class="band--amber" d="M0,925 C100,945 200,955 292,960 H0 Z"/>
      <path class="band--navy" d="M0,925 C50,940 95,952 142,960 H0 Z"/>
    </svg>

    <ul class="contact">
      <li class="contact__item">
        <svg class="contact__icon contact__icon--solid" viewBox="0 0 10 10"><path d="M2,0.5 L3.6,2.8 L2.6,3.8 C3.2,5.2 4.8,6.8 6.2,7.4 L7.2,6.4 L9.5,8 L8.3,9.5 C4.5,9.3 0.7,5.5 0.5,1.7 Z"/></svg>
        <span>672-330-4185</span>
      </li>
      <li class="contact__item">
        <svg class="contact__icon" viewBox="0 0 10 10"><rect x="0.8" y="2" width="8.4" height="6" rx="0.8"/><path d="M1,2.4 L5,5.4 L9,2.4"/></svg>
        <span>hello@rtamofiji.example</span>
      </li>
      <li class="contact__item">
        <svg class="contact__icon" viewBox="0 0 10 10"><circle cx="5" cy="5" r="4"/><ellipse cx="5" cy="5" rx="1.8" ry="4"/><path d="M1,5 H9"/></svg>
        <span>rtamofiji.example</span>
      </li>
    </ul>

    <div class="brand">R.Tamo Fiji</div>

    <div class="watermark" aria-hidden="true">R.Tamo Fiji</div>
  </main>
</body>
</html>
```